GlintOn Feather Line Toothbrush Backcard Design

We need a toothbrush backcard (toothbrush packaging) design for our new toothbrush. We are one of the leading toothbrush distributor and producer company. At the moment our toothbrushes are selling at Quinby, Kindred Mart, 4-Bright and many more supermarkets and mom-and-pop shops in Thailand. Our toothbrush is emphasized on the soft and slim tip bristles which will not hurt your enamel. Easy to grip handle that will ease of use. These 2 mains point should be communicated through the design.

Our brand name is GlintOn (see attached logo that you can use) and the toothbrush model is Feather Line. We will have 2 series for this model which are Feather Line Extra Soft and Feather Line Medium soft. They are basically differentiated by its packaging colors.

We are looking for the attractive and outstanding design from what available in the market right now. Please see enclosed die cut shape of the packaging. This backcard will hold 3 pieces of toothbrush with clear blister cover.

P.S We are very confident that our product produced with very good quality that's why we want to attract people to try. So when they walk in the aisle we want our toothbrush packaging to be eye catching and welcome customer to try.

Target Market(s)

B+ household consumers age between 18-65 both men and women who has open minded to the new product and willing to spend money without brand royalty.

Font styles to use
Sans Serif

Colors

Designer to choose colors to be used in the design.

Requirements
Must have
• - Logo, and model name
• - Quality mark as following GMP, FDA, ISO9001:2015, ISO22176
• - Attractive character which attract the target clients to try.
• - 2-sided packaging using attached die cut
Nice to have
Should not have
• What other brands have

```html
<!DOCTYPE html>
<html lang="en">
<head>
<meta charset="utf-8">
<title>GlintOn Feather Line Backcards</title>
<link href="https://fonts.googleapis.com/css2?family=Baloo+2:wght@600;800&family=Montserrat:wght@700;800&display=swap" rel="stylesheet">
<style>
  :root {
    --page: #ffffff;
    --plum-dark: #55214c;
    --plum-mid: #9a2c8e;
    --plum-glow: #c85aa8;
    --navy-dark: #272d4c;
    --sky-mid: #0aa6e2;
    --sky-glow: #5fd0f7;
    --blister-line: #2fa8e8;
    --label-yellow: #f8c51e;
    --label-edge: #f39c16;
    --pill-plum: #5a2c6c;
    --pill-navy: #29306e;
    --ink-dark: #3c3c3e;
    --white: #ffffff;
    --brush-white: rgba(255, 255, 255, 0.28);
    --brush-mint: rgba(143, 224, 198, 0.32);
  }
  * { box-sizing: border-box; margin: 0; padding: 0; }
  html, body { width: 833px; height: 1200px; overflow: hidden; background: var(--page); }
  body { position: relative; font-family: "Montserrat", sans-serif; }

  .backcard { position: absolute; top: 50px; width: 375px; height: 1114px; overflow: hidden; }
  .backcard--extra { left: 38px; background: linear-gradient(180deg, var(--plum-dark) 0%, var(--plum-mid) 58%, var(--plum-dark) 100%); }
  .backcard--medium { left: 434px; background: linear-gradient(180deg, var(--navy-dark) 0%, var(--sky-mid) 58%, var(--navy-dark) 100%); }

  .backcard__glow { position: absolute; left: 70px; top: 420px; width: 240px; height: 240px; border-radius: 50%; }
  .backcard--extra .backcard__glow { background: radial-gradient(circle, var(--plum-glow) 0%, rgba(200,90,168,0) 70%); }
  .backcard--medium .backcard__glow { background: radial-gradient(circle, var(--sky-glow) 0%, rgba(95,208,247,0) 70%); }

  .blister { position: absolute; inset: 0; }

  .brand-mark {
    position: absolute; top: 176px; left: 0; width: 100%; text-align: center;
    font-family: "Baloo 2", sans-serif; font-weight: 800; font-size: 42px; letter-spacing: 1px;
    color: var(--white);
  }

  .brush-area {
    position: absolute; left: 62px; top: 252px; width: 250px; height: 838px;
    border-radius: 34px 34px 20px 20px;
    background: linear-gradient(180deg, var(--brush-white) 0%, var(--brush-white) 18%, rgba(255,255,255,0.12) 40%, var(--brush-mint) 62%, var(--brush-white) 100%);
  }

  .pack-label {
    position: absolute; left: 71px; top: 666px; width: 235px; height: 348px;
    background: var(--label-yellow); border-radius: 18px;
    box-shadow: inset 0 0 0 3px var(--label-edge);
    overflow: hidden;
  }
  .series-pill {
    position: absolute; left: 12px; top: 12px; width: 212px; height: 62px;
    border-radius: 30px 30px 30px 0; display: flex; align-items: center; justify-content: center; gap: 6px;
    color: var(--white);
  }
  .backcard--extra .series-pill, .backcard--extra .pack-count { background: var(--pill-plum); }
  .backcard--medium .series-pill, .backcard--medium .pack-count { background: var(--pill-navy); }
  .series-pill__line { font-size: 12.5px; font-weight: 800; line-height: 1.15; text-align: right; }
  .series-pill__grade { font-family: "Baloo 2", sans-serif; font-style: italic; font-weight: 800; font-size: 38px; line-height: 1; }
  .pack-count {
    position: absolute; left: 12px; top: 74px; width: 104px; height: 38px;
    border-radius: 0 0 20px 20px; color: var(--white);
    font-weight: 800; font-style: italic; font-size: 23px; line-height: 38px; text-align: center;
  }
  .label-band {
    position: absolute; left: -24px; top: 120px; width: 290px; height: 112px;
    background: var(--white); border-radius: 50% 50% 50% 50% / 30% 30% 60% 60%;
    transform: rotate(-8deg);
  }
  .label-brand {
    position: absolute; left: 0; top: 146px; width: 100%; text-align: center;
    font-family: "Baloo 2", sans-serif; font-weight: 800; font-size: 46px; line-height: 1; color: var(--ink-dark);
    transform: rotate(-8deg);
  }
  .feature-badges { position: absolute; left: 9px; top: 240px; width: 217px; height: 100px; }
</style>
</head>
<body>

  <section class="backcard backcard--extra">
    <div class="backcard__glow"></div>
    <svg class="blister" viewBox="0 0 375 1114" aria-hidden="true">
      <rect x="24" y="21" width="326" height="1057" rx="40" fill="none" stroke="var(--blister-line)" stroke-width="1.5"/>
      <rect x="45" y="44" width="284" height="1012" rx="30" fill="none" stroke="var(--blister-line)" stroke-width="1.5"/>
      <path d="M150 80 H305 V132 H150 A14 14 0 0 1 136 118 V94 A14 14 0 0 1 150 80 Z M170 108 q15 -14 30 0 t30 0 t30 0 t30 0" fill="none" stroke="var(--blister-line)" stroke-width="1.5"/>
    </svg>
    <div class="brand-mark">GlintOn</div>
    <div class="brush-area" role="img" aria-label="Three white toothbrushes with mint comfort grips held under a clear blister"></div>
    <div class="pack-label">
      <div class="series-pill">
        <span class="series-pill__line">Feather Line<br>Extra</span>
        <span class="series-pill__grade">Soft</span>
      </div>
      <div class="pack-count">3Pack</div>
      <div class="label-band"></div>
      <div class="label-brand">GlintOn</div>
      <svg class="feature-badges" viewBox="0 0 217 100" aria-label="Comfort grip handle, soft and slim tip bristles">
        <defs>
          <path id="arcA1" d="M10 58 A40 40 0 0 1 90 58"/>
          <path id="arcB1" d="M127 58 A40 40 0 0 1 207 58"/>
        </defs>
        <circle cx="50" cy="58" r="44" fill="var(--white)"/>
        <circle cx="50" cy="62" r="26" fill="none" stroke="var(--pill-plum)" stroke-width="2.5"/>
        <path d="M34 66 H64 M60 58 v8" stroke="var(--ink-dark)" stroke-width="3" stroke-linecap="round"/>
        <text font-family="Montserrat, sans-serif" font-weight="800" font-size="8" fill="var(--ink-dark)"><textPath href="#arcA1" startOffset="50%" text-anchor="middle">COMFORT GRIP HANDLE</textPath></text>
        <circle cx="167" cy="58" r="44" fill="var(--white)"/>
        <circle cx="167" cy="62" r="26" fill="none" stroke="var(--pill-plum)" stroke-width="2.5"/>
        <path d="M156 56 q11 -8 22 0 v13 l-5 8 l-6 -6 l-6 6 l-5 -8 Z" fill="none" stroke="var(--ink-dark)" stroke-width="2"/>
        <text font-family="Montserrat, sans-serif" font-weight="800" font-size="7.5" fill="var(--ink-dark)"><textPath href="#arcB1" startOffset="50%" text-anchor="middle">SOFT &amp; SLIM TIP BRISTLES</textPath></text>
      </svg>
    </div>
  </section>

  <section class="backcard backcard--medium">
    <div class="backcard__glow"></div>
    <svg class="blister" viewBox="0 0 375 1114" aria-hidden="true">
      <rect x="24" y="21" width="326" height="1057" rx="40" fill="none" stroke="var(--blister-line)" stroke-width="1.5"/>
      <rect x="45" y="44" width="284" height="1012" rx="30" fill="none" stroke="var(--blister-line)" stroke-width="1.5"/>
      <path d="M150 80 H305 V132 H150 A14 14 0 0 1 136 118 V94 A14 14 0 0 1 150 80 Z M170 108 q15 -14 30 0 t30 0 t30 0 t30 0" fill="none" stroke="var(--blister-line)" stroke-width="1.5"/>
    </svg>
    <div class="brand-mark">GlintOn</div>
    <div class="brush-area" role="img" aria-label="Three white toothbrushes with mint comfort grips held under a clear blister"></div>
    <div class="pack-label">
      <div class="series-pill">
        <span class="series-pill__line">Feather Line<br>Medium</span>
        <span class="series-pill__grade">soft</span>
      </div>
      <div class="pack-count">3Pack</div>
      <div class="label-band"></div>
      <div class="label-brand">GlintOn</div>
      <svg class="feature-badges" viewBox="0 0 217 100" aria-label="Comfort grip handle, soft and slim tip bristles">
        <defs>
          <path id="arcA2" d="M10 58 A40 40 0 0 1 90 58"/>
          <path id="arcB2" d="M127 58 A40 40 0 0 1 207 58"/>
        </defs>
        <circle cx="50" cy="58" r="44" fill="var(--white)"/>
        <circle cx="50" cy="62" r="26" fill="none" stroke="var(--pill-plum)" stroke-width="2.5"/>
        <path d="M34 66 H64 M60 58 v8" stroke="var(--ink-dark)" stroke-width="3" stroke-linecap="round"/>
        <text font-family="Montserrat, sans-serif" font-weight="800" font-size="8" fill="var(--ink-dark)"><textPath href="#arcA2" startOffset="50%" text-anchor="middle">COMFORT GRIP HANDLE</textPath></text>
        <circle cx="167" cy="58" r="44" fill="var(--white)"/>
        <circle cx="167" cy="62" r="26" fill="none" stroke="var(--pill-plum)" stroke-width="2.5"/>
        <path d="M156 56 q11 -8 22 0 v13 l-5 8 l-6 -6 l-6 6 l-5 -8 Z" fill="none" stroke="var(--ink-dark)" stroke-width="2"/>
        <text font-family="Montserrat, sans-serif" font-weight="800" font-size="7.5" fill="var(--ink-dark)"><textPath href="#arcB2" startOffset="50%" text-anchor="middle">SOFT &amp; SLIM TIP BRISTLES</textPath></text>
      </svg>
    </div>
  </section>

</body>
</html>
```